Bottle Label for Premium Gold CBD Oil

10 ml CBD-Oil bottle. The job is pretty straight forward and everything you need is prepared. However, the design part of the creative part ^^ The design of a lot of follow-up products we could do together. We thought about an exclusive / minimalist approach to Morvo. The bottle itself is delivered in a drawer box which looks much better than the cheap packages of the competition. Everything about the product is supposed to be honest and of high quality. The product is even more cost-effective than CBD-Oils. Key feature of the product is its deeply golden color. The design should be in harmony with this color. The customer pays a high price for this little bottle and has high expectations. Accordingly, the label should express itself and the product is worth every cent. Which it is by the way. If you would like to see the labels of the competition, just type in "CBD OIL" on "warenzelt.de". However, we are currently the only ones with a new filtration and the corresponding golden color. This label is going to be the base of a whole series of products. If we are happy with your label design, we will do a lot of following up designs with you. The logo design is already done and just needs to be implemented. We are looking forward to your designs. Many, many thanks in advance
Target Market(s)
Customers who want to use the absolute top CBD product on the market in order to improve their health
Colors
Designer to choose colors to be used in the design.
Requirements
Must have
- Please read the pdf-file with detailed descriptions and pictures. The costomer should always see that our product is of the highest quality. Please feel free to stick to our suggestions / ideas since I we are no designers. If you have your own cool approach, just submit it ^^
Nice to have
- We think it would be nice to have a drop out on the front of the label. We could imagine an exclusive / minimalist approach similar to Morvo

```html
<!DOCTYPE html>
<html lang="de">
<head>
<meta charset="utf-8">
<title>Premium Gold CBD-Hanföl – Etikett</title>
<link href="https://fonts.googleapis.com/css2?family=Cinzel:wght@400&family=Roboto:ital,wght@0,300;0,400;0,500;1,300&family=Roboto+Condensed:wght@300&family=Arimo:wght@400&display=swap" rel="stylesheet">
<style>
  :root {
    --stage: #2a2a2a;
    --label: #f2f2f2;
    --label-shade: #e4e4e4;
    --ink: #1f1f1f;
    --ink-soft: #3a3a3a;
    --band: #141414;
    --gold: #e0731f;
    --gold-deep: #c2501a;
    --white: #ffffff;
  }
  * { margin: 0; padding: 0; box-sizing: border-box; }
  html, body { width: 1200px; height: 900px; overflow: hidden; }
  body { background: var(--stage); position: relative; }

  .label {
    position: absolute;
    top: 197px;
    width: 340px;
    height: 506px;
    background: linear-gradient(90deg, var(--label) 0%, var(--white) 45%, var(--label-shade) 100%);
    overflow: hidden;
  }
  .label--front { left: 220px; }
  .label--back { left: 640px; }

  /* front */
  .brand {
    position: absolute;
    top: 48px; left: 0; right: 0;
    text-align: center;
    font-family: "Cinzel", serif;
    font-weight: 400;
    color: var(--ink-soft);
  }
  .brand__dot {
    display: block;
    width: 40px; height: 40px;
    margin: 0 auto 14px;
    border-radius: 50%;
    background: var(--gold);
  }
  .brand__name { font-size: 23px; line-height: 29px; letter-spacing: 1px; }

  .front-art { position: absolute; inset: 0; }

  .product-type {
    position: absolute;
    top: 234px; left: 0; right: 0;
    text-align: center;
    font-family: "Roboto", sans-serif;
    color: var(--ink);
  }
  .product-type__spectrum { font-size: 26px; font-weight: 300; line-height: 32px; }
  .product-type__name { font-size: 24px; font-weight: 500; line-height: 30px; }

  .strength {
    position: absolute;
    top: 330px; left: 38px;
    font-family: "Roboto", sans-serif;
    font-weight: 400;
    font-size: 36px;
    color: var(--white);
    line-height: 1;
  }
  .strength sup { font-size: 18px; vertical-align: 16px; }
  .edition {
    position: absolute;
    top: 334px; left: 155px;
    font-family: "Roboto", sans-serif;
    font-style: italic;
    font-weight: 300;
    font-size: 23px;
    color: var(--white);
  }
  .contents {
    position: absolute;
    top: 468px; left: 0; right: 0;
    text-align: center;
    font-family: "Roboto Condensed", sans-serif;
    font-weight: 300;
    font-size: 18px;
    color: var(--ink);
    word-spacing: 1px;
  }

  /* back */
  .back-band {
    position: absolute;
    top: 314px; height: 62px;
    background: var(--band);
  }
  .back-band--left { left: 0; width: 159px; }
  .back-band--right { left: 176px; width: 164px; }
  .divider {
    position: absolute;
    top: 0; bottom: 0; left: 159px; width: 17px;
    background: var(--white);
  }
  .divider::after {
    content: "";
    position: absolute;
    top: 0; bottom: 0; left: 1px; width: 13px;
    background: linear-gradient(90deg, var(--gold-deep), var(--gold));
  }
  .info {
    position: absolute;
    top: 40px;
    height: 262px;
    writing-mode: vertical-rl;
    transform: rotate(180deg);
    font-family: "Arimo", sans-serif;
    font-size: 16.5px;
    line-height: 21.5px;
    color: var(--ink);
    white-space: nowrap;
  }
  .info--usage { left: 52px; width: 86px; }
  .info--origin { left: 190px; width: 108px; }
</style>
</head>
<body>

<section class="label label--front" aria-label="Etikett Vorderseite">
  <svg class="front-art" width="340" height="506" viewBox="0 0 340 506" aria-hidden="true">
    <path d="M12 315 C 28 175, 300 150, 330 315 L 320 315 C 292 185, 44 196, 16 315 Z" fill="var(--ink)"/>
    <rect x="0" y="315" width="340" height="61" fill="var(--band)"/>
    <defs>
      <linearGradient id="dropFill" x1="0" x2="1" y1="0" y2="0">
        <stop offset="0" stop-color="#f08a3a"/>
        <stop offset="1" stop-color="#c9541a"/>
      </linearGradient>
    </defs>
    <path d="M124 326 C 140 370, 167 394, 167 418 A 43 43 0 0 1 81 418 C 81 394, 108 370, 124 326 Z"
          fill="url(#dropFill)" stroke="var(--ink)" stroke-width="2"/>
    <path d="M110 404 C 114 414, 121 419, 121 426 A 11 11 0 0 1 99 426 C 99 419, 106 414, 110 404 Z"
          fill="var(--ink)"/>
  </svg>

  <div class="brand">
    <span class="brand__dot"></span>
    <div class="brand__name">Goldtal<br>Hanfwerkstatt</div>
  </div>

  <div class="product-type">
    <div class="product-type__spectrum">Vollspektum</div>
    <div class="product-type__name">CBD-HANFÖL</div>
  </div>

  <div class="strength">10<sup>%</sup></div>
  <div class="edition">Premium Gold</div>

  <div class="contents">10 ml &nbsp;•&nbsp; 250 Tropfen &nbsp;•&nbsp; 1000 mg CBD</div>
</section>

<section class="label label--back" aria-label="Etikett Rückseite">
  <div class="back-band back-band--left"></div>
  <div class="back-band back-band--right"></div>
  <div class="divider"></div>

  <p class="info info--usage">Anwendung:<br>2 x 3 Tropfen täglich<br>THC-Gehalt &lt; 0,05 %<br>Vor Licht und Wärme schützen</p>
  <p class="info info--origin">Hergestellt in Deutschland<br>Produzent: Kornblatt GmbH,<br>Talheim<br>Charge:<br>Mind. haltbar bis:</p>
</section>

</body>
</html>
```